Managed Service Provider email

We need an email designed that advertises our Managed Services product. We have been in business 28 years. Managed Services includes proactive ticketing, Help desk support, server and workstation monitoring, data backup monitoring, spam protection, regular reports, Worklane 720, telecom services, ISP management, vendor management and more.

Target Market(s)

Business owners, decision makers, IT, CTO

Industry/Entity Type

Information Technology

Colors

Designer to choose colors to be used in the design.

Requirements
Must have
• Bullet points with included services. Mention of 28 years in business.
Nice to have
• We'd love our designer to read up on what an MSP (Managed Service Provider) does and use that information to find/create content for our email project.
Should not have
• A picture of a computer with a thermometer in its mouth.

```html
<!DOCTYPE html>
<html lang="en">
<head>
<meta charset="utf-8">
<title>Corvane Network Services – Managed Services</title>
<link href="https://fonts.googleapis.com/css2?family=Roboto:wght@300;400;500;700&display=swap" rel="stylesheet">
<style>
  :root {
    --blue: #1f6fd1;
    --blue-deep: #0d4fa8;
    --blue-light: #3f8ee6;
    --navy: #0b2a5a;
    --ink: #222222;
    --grey: #555555;
    --footer: #0a0a0a;
    --white: #ffffff;
    --red: #c8202f;
  }
  * { margin: 0; padding: 0; box-sizing: border-box; }
  html, body { width: 1200px; height: 2248px; overflow: hidden; background: var(--white); }
  body { font-family: "Roboto", Arial, sans-serif; color: var(--ink); position: relative; }

  .hero {
    position: absolute; left: 0; top: 0; width: 1200px; height: 760px;
    background: linear-gradient(160deg, #2b3a4c 0%, #18212d 45%, #0f1722 100%);
    overflow: hidden;
  }
  .hero-photo {
    position: absolute; inset: 0;
    background: radial-gradient(ellipse at 30% 40%, rgba(220,200,170,0.35) 0%, rgba(60,80,100,0.2) 35%, rgba(0,0,0,0) 65%),
                linear-gradient(90deg, rgba(10,15,25,0.2), rgba(40,60,80,0.35) 60%, rgba(10,15,25,0.6));
  }
  .topbar {
    position: absolute; left: 0; top: 40px; width: 100%; height: 80px;
    display: flex; align-items: center; justify-content: space-between; padding: 0 56px;
    color: var(--white);
  }
  .topbar-phone { display: flex; align-items: center; gap: 14px; font-size: 22px; }
  .brand {
    position: absolute; left: 50%; top: 44px; transform: translateX(-50%);
    display: flex; align-items: center; gap: 14px;
    font-size: 52px; font-weight: 500; color: var(--white); letter-spacing: 1px;
  }
  .brand-mark { width: 26px; height: 26px; background: var(--white); border-radius: 50%; }
  .top-social { display: flex; gap: 12px; }
  .top-social span { width: 26px; height: 26px; background: var(--white); border-radius: 3px; display: block; }
  .hero-title {
    position: absolute; left: 0; width: 100%; top: 610px; text-align: center; color: var(--white);
  }
  .hero-title h1 { font-size: 50px; font-weight: 500; }
  .hero-title p { font-size: 38px; font-weight: 400; margin-top: 14px; }
  .hero-curve { position: absolute; left: 0; top: 690px; width: 1200px; height: 120px; }

  .welcome { position: absolute; left: 0; top: 770px; width: 100%; text-align: center; }
  .welcome h2 { font-size: 44px; font-weight: 400; color: var(--ink); }
  .welcome p {
    width: 1110px; margin: 28px auto 0; font-size: 21px; line-height: 33px; color: var(--grey); font-weight: 300;
  }
  .btn {
    display: inline-block; margin-top: 26px; padding: 8px 32px;
    background: var(--navy); color: var(--white); font-size: 20px; border-radius: 4px;
  }

  .services { position: absolute; left: 0; top: 1040px; width: 1200px; height: 600px; }
  .services-bg { position: absolute; inset: 0; }
  .services h2 {
    position: absolute; left: 0; top: 120px; width: 100%; text-align: center;
    color: var(--white); font-size: 48px; font-weight: 400;
  }
  .service-list { position: absolute; top: 250px; list-style: none; color: var(--white); font-size: 26px; }
  .service-list li { height: 52px; display: flex; align-items: center; gap: 16px; }
  .service-list li::before {
    content: ""; width: 12px; height: 12px; border-radius: 50%; background: var(--white); flex: none;
  }
  .list-left { left: 90px; }
  .list-right { left: 850px; }
  .services-art {
    position: absolute; left: 440px; top: 220px; width: 320px; height: 230px; border-radius: 10px;
    background: linear-gradient(180deg, #e9f2fb 0%, #b9d3ee 100%);
  }

  .partners { position: absolute; left: 0; top: 1640px; width: 100%; text-align: center; }
  .partners h2 { font-size: 42px; font-weight: 400; }
  .partner-row { display: flex; justify-content: center; align-items: center; gap: 60px; margin-top: 60px; }
  .partner-badge { width: 180px; height: 70px; background: #e3e6ea; border-radius: 6px; }
  .partner-badge.round { width: 80px; height: 80px; border-radius: 50%; }

  .footer { position: absolute; left: 0; top: 1980px; width: 1200px; height: 268px; }
  .footer-bg { position: absolute; inset: 0; }
  .footer-content { position: absolute; left: 0; top: 100px; width: 100%; text-align: center; color: var(--white); }
  .footer-address { display: flex; justify-content: center; align-items: center; gap: 10px; font-size: 20px; }
  .footer-social { display: flex; justify-content: center; gap: 14px; margin-top: 22px; }
  .footer-social span { width: 34px; height: 34px; border: 2px solid var(--white); border-radius: 50%; display: block; }
  .footer-copy { font-size: 18px; margin-top: 20px; }
</style>
</head>
<body>

<header class="hero">
  <div class="hero-photo" role="img" aria-label="Photo of a technician with a tablet in a server room"></div>
  <div class="topbar">
    <div class="topbar-phone">
      <svg width="22" height="22" viewBox="0 0 24 24"><rect x="1" y="1" width="22" height="22" rx="3" fill="#fff"/><path d="M8 6c-1 1-1 3 1 6s5 5 7 5l1.5-2-2.5-1.5-1 1c-1.5-.5-3-2-3.5-3.5l1-1L10 7z" fill="#1a2330"/></svg>
      <span>555-014-2290</span>
    </div>
    <div class="top-social"><span></span><span></span><span></span><span></span></div>
  </div>
  <div class="brand"><span class="brand-mark"></span>Corvane</div>
  <div class="hero-title">
    <h1>Corvane Network Services</h1>
    <p>28 years in business</p>
  </div>
  <svg class="hero-curve" viewBox="0 0 1200 120" preserveAspectRatio="none">
    <path d="M0 20 Q600 110 1200 20 L1200 120 L0 120 Z" fill="#fff"/>
    <path d="M0 20 Q600 110 1200 20" fill="none" stroke="#1f6fd1" stroke-width="6"/>
  </svg>
</header>

<section class="welcome">
  <h2>Welcome to Corvane Network Services</h2>
  <p>It is a long established fact that a reader will be distracted by the readable content of a page when looking at its layout. The point of using Lorem Ipsum is that it has a more-or-less normal distribution of letters, as opposed to using 'Content here, content here', making it look like readable English</p>
  <span class="btn">View More</span>
</section>

<section class="services">
  <svg class="services-bg" viewBox="0 0 1200 600" preserveAspectRatio="none">
    <defs>
      <linearGradient id="svcGrad" x1="0" y1="0" x2="0" y2="1">
        <stop offset="0" stop-color="#3f8ee6"/>
        <stop offset="1" stop-color="#0d4fa8"/>
      </linearGradient>
    </defs>
    <path d="M0 40 Q600 120 1200 40 L1200 540 Q600 620 0 540 Z" fill="url(#svcGrad)"/>
  </svg>
  <h2>Our Services</h2>
  <ul class="service-list list-left">
    <li>Proactive ticketing</li>
    <li>Help desk support</li>
    <li>Server and workstation...</li>
    <li>Data backup monitoring</li>
    <li>Spam protection</li>
  </ul>
  <div class="services-art" role="img" aria-label="Illustration of a monitor showing charts with a tablet and magnifier"></div>
  <ul class="service-list list-right">
    <li>Regular reports</li>
    <li>Worklane 720</li>
    <li>Telecom services</li>
    <li>ISP management</li>
    <li>Vendor management</li>
  </ul>
</section>

<section class="partners">
  <h2>Partners</h2>
  <div class="partner-row">
    <span class="partner-badge"></span>
    <span class="partner-badge"></span>
    <span class="partner-badge round"></span>
    <span class="partner-badge"></span>
  </div>
</section>

<footer class="footer">
  <svg class="footer-bg" viewBox="0 0 1200 268" preserveAspectRatio="none">
    <path d="M0 50 Q600 0 1200 50 L1200 268 L0 268 Z" fill="#1f6fd1"/>
    <path d="M0 62 Q600 12 1200 62 L1200 268 L0 268 Z" fill="#0a0a0a"/>
  </svg>
  <div class="footer-content">
    <div class="footer-address">
      <svg width="16" height="22" viewBox="0 0 16 22"><path d="M8 0C3.6 0 0 3.4 0 7.6 0 13 8 22 8 22s8-9 8-14.4C16 3.4 12.4 0 8 0zm0 10.5A3 3 0 1 1 8 4.5a3 3 0 0 1 0 6z" fill="#fff"/></svg>
      <span>418 N Alder Ave Brookfield, MO 65990</span>
    </div>
    <div class="footer-social"><span></span><span></span><span></span><span></span><span></span><span></span></div>
    <p class="footer-copy">Copyright © 2018, All Rights Reserved</p>
  </div>
</footer>

</body>
</html>
```